Food broker, trader, wholesaler, liquidator looking for a 5 pages website

Looking for a 5 pages website design. We are food brokers, traders, wholesaler and closeout buyer working with manufacturers, distributors, importers sell to retailers, food service operators and industrial (ingredients). We help market their products. We are a resource for those who need a solution in the distribution/selling/placement of food on the shelves, kitchens and pantries. Whether we open new accounts with new products or sell short dated inventory, we know where to go and get results.

Target Market(s)

Food manufacturers, food distributors, food brokers

Coding

Coded - Design and coding required

Number of Pages Required

4 page

Font styles to use
Serif

Requirements
Must have
• Food-food production-warehouse-Food packaging-people meeting-trucks-supermarket shelves-

```html
<!DOCTYPE html>
<html lang="en">
<head>
<meta charset="utf-8">
<title>Harborline Provisions — Food Brokers, Traders and Wholesaler</title>
<link href="https://fonts.googleapis.com/css2?family=Outfit:wght@300;400;500;600&display=swap" rel="stylesheet">
<style>
:root{
  --navy:#14146a;
  --orange:#f9ab30;
  --ink:#1d1d3a;
  --muted:#6b6b78;
  --footer:#e8eef3;
  --white:#ffffff;
}
*{box-sizing:border-box;margin:0;padding:0}
html,body{width:1200px;height:2665px;overflow:hidden}
body{position:relative;font-family:'Outfit',sans-serif;color:var(--ink);background:var(--white)}
.abs{position:absolute}
a{text-decoration:none;color:inherit}

/* header */
.brand{left:88px;top:10px;width:150px;text-align:center}
.brand-mark{width:84px;height:66px;border-radius:50%;background:var(--navy);margin:0 auto 6px}
.brand-name{font-size:12px;font-weight:600;color:var(--navy);letter-spacing:.3px}
.nav{top:40px;left:342px;display:flex;gap:37px;font-size:14px;color:#333}
.nav .active{color:var(--orange)}
.call{top:39px;left:768px;font-size:15px;font-weight:500;color:var(--orange);display:flex;align-items:center;gap:6px}
.call b{color:var(--navy);font-weight:500}
.btn{display:inline-flex;align-items:center;justify-content:center;border-radius:20px;font-size:14px}
.btn-navy{background:var(--navy);color:var(--white)}
.btn-orange{background:var(--orange);color:var(--navy)}
.btn-white{background:var(--white);color:var(--navy)}
.giving{left:984px;top:32px;width:128px;height:32px}

/* hero */
.hero{left:0;top:96px;width:1200px;height:543px;background:linear-gradient(110deg,#8c9aa6 0%,#c9d2d9 35%,#e8ecef 55%,#b7a78e 80%,#9c7a52 100%)}
.hero-shade{left:0;top:96px;width:620px;height:543px;background:linear-gradient(90deg,rgba(20,20,50,.35),rgba(20,20,50,0))}
.hero-title{left:88px;top:264px;width:460px;font-size:30px;font-weight:500;line-height:1.18;color:var(--white)}
.hero-text{left:88px;top:347px;width:440px;font-size:14.5px;font-weight:500;line-height:1.35;color:var(--white)}
.hero-cta{left:89px;top:432px;width:127px;height:32px}
.arrow-btn{width:32px;height:32px;border-radius:50%;display:flex;align-items:center;justify-content:center}
.prev{left:1080px;top:332px;background:rgba(255,255,255,.8)}
.next{left:1080px;top:372px;background:var(--orange)}
.seal{left:550px;top:600px;width:100px;height:76px;border-radius:50%;background:var(--navy);border:6px solid var(--white)}

/* about */
.about-photo{left:88px;top:719px;width:433px;height:433px;border-radius:50%;background:radial-gradient(circle at 50% 45%,#e9e9ec 0%,#c9c5c0 45%,#a26a4c 75%,#8a8f97 100%)}
.eyebrow{left:617px;top:785px;font-size:15px;color:var(--orange)}
.about-title{left:616px;top:803px;font-size:30px;font-weight:500;color:var(--navy)}
.about-lead{left:616px;top:852px;width:460px;font-size:13px;font-weight:500;line-height:1.45;color:var(--ink)}
.about-sub{left:616px;top:910px;font-size:13px;font-weight:500;color:var(--ink)}
.about-body{left:616px;top:948px;width:500px;font-size:13.5px;font-weight:300;line-height:1.42;color:var(--muted)}
.about-cta{left:617px;top:1051px;width:128px;height:32px}

/* services */
.services{left:0;top:1231px;width:1200px;height:581px;background:var(--navy)}
.services-title{left:0;top:1303px;width:1200px;text-align:center;font-size:30px;font-weight:500;color:var(--white)}
.card{top:1374px;width:320px;height:360px}
.card-img{position:absolute;left:0;top:0;width:320px;height:240px}
.card-cover{position:absolute;left:0;top:201px;width:280px;height:160px;background:var(--navy);border-top:3px solid var(--orange)}
.card-title{position:absolute;left:24px;top:229px;font-size:19px;font-weight:500;color:var(--white)}
.card-text{position:absolute;left:24px;top:268px;width:270px;font-size:13.5px;font-weight:300;line-height:1.35;color:var(--white)}
.card-btn{position:absolute;left:24px;top:326px;width:80px;height:31px}
.img-sales{background:linear-gradient(135deg,#d9cbb6,#8a6a4a 60%,#3d3a3a)}
.img-trade{background:linear-gradient(160deg,#c9d3da,#b8442e 40%,#c79a52 65%,#5f7b8a)}
.img-shelf{background:linear-gradient(120deg,#e25c3a,#f3d15b 35%,#e8ecef 55%,#2f6fb3 85%)}

/* why */
.why-title{left:0;top:1882px;width:1170px;text-align:center;font-size:30px;font-weight:500;color:var(--navy)}
.why-text{left:230px;top:1944px;width:710px;text-align:center;font-size:13.5px;font-weight:300;line-height:1.42;color:var(--muted)}
.feature{top:2029px;width:200px;text-align:center}
.feature-icon{width:80px;height:80px;border-radius:50%;border:1.5px solid var(--orange);margin:0 auto;display:flex;align-items:center;justify-content:center}
.feature-label{margin-top:18px;font-size:15px;font-weight:500;color:var(--navy)}

/* footer */
.footer{left:0;top:2219px;width:1200px;height:446px;background:var(--footer)}
.f-head{top:2303px;font-size:17px;font-weight:500;color:var(--navy)}
.f-call{left:89px;top:2347px;font-size:19px;color:var(--orange);display:flex;align-items:center;gap:6px;font-weight:300}
.f-call b{color:var(--navy);font-weight:300}
.f-mail{left:89px;top:2372px;font-size:13px;font-weight:300;color:#444}
.f-loc-label{left:89px;top:2410px;font-size:13px;color:var(--orange);font-weight:300}
.f-loc{left:89px;top:2428px;width:260px;font-size:13.5px;line-height:1.42;font-weight:300;color:#444}
.f-links{left:407px;top:2345px;font-size:13px;font-weight:300;color:#444;line-height:29px;list-style:none}
.field{border:1px solid #9aa3b6;border-radius:17px;font-size:12px;color:#555;padding:10px 13px;font-weight:300}
.f-name{left:585px;top:2353px;width:163px;height:32px}
.f-phone{left:767px;top:2353px;width:163px;height:32px}
.f-email{left:948px;top:2353px;width:164px;height:32px}
.f-msg{left:585px;top:2405px;width:527px;height:95px;border-radius:20px}
.f-send{left:585px;top:2520px;width:128px;height:31px}
.social{top:2519px;width:32px;height:32px;border-radius:50%;border:1px solid var(--orange)}
.social.on{background:var(--orange)}
.copy{left:89px;top:2598px;font-size:13px;font-weight:300;color:#444}
.to-top{left:1094px;top:2590px}
</style>
</head>
<body>

<header>
  <div class="abs brand"><div class="brand-mark"></div><div class="brand-name">HARBORLINE PROVISIONS</div></div>
  <nav class="abs nav">
    <a class="active" href="#">-- Home --</a><a href="#">About Us</a><a href="#">What We Do</a><a href="#">Contact Us</a>
  </nav>
  <div class="abs call">Call Us:
    <svg width="16" height="16" viewBox="0 0 24 24" fill="none" stroke="#f9ab30" stroke-width="2"><path d="M22 16.9v3a2 2 0 0 1-2.2 2 19.8 19.8 0 0 1-8.6-3.1 19.5 19.5 0 0 1-6-6A19.8 19.8 0 0 1 2.1 4.2 2 2 0 0 1 4.1 2h3a2 2 0 0 1 2 1.7c.1.9.4 1.8.7 2.7a2 2 0 0 1-.5 2.1L8 9.8a16 16 0 0 0 6 6l1.3-1.3a2 2 0 0 1 2.1-.4c.9.3 1.8.6 2.7.7a2 2 0 0 1 1.7 2z"/></svg>
    <b>555-014-2290</b></div>
  <a class="abs btn btn-navy giving" href="#">Giving Back</a>
</header>

<section>
  <div class="abs hero" role="img" aria-label="Food production staff in white coats and hairnets packing baked goods on trays"></div>
  <div class="abs hero-shade"></div>
  <h1 class="abs hero-title">We are Food Brokers, Traders and Wholesaler</h1>
  <p class="abs hero-text">Closeout buyer working with manufacturers, distributors, importers sell to retailers, food service operators and industrial (ingredients).</p>
  <a class="abs btn btn-orange hero-cta" href="#">Contact Us</a>
  <div class="abs arrow-btn prev"><svg width="10" height="10" viewBox="0 0 10 10"><path d="M6.5 1.5 3 5l3.5 3.5" stroke="#14146a" fill="none" stroke-width="1.3"/></svg></div>
  <div class="abs arrow-btn next"><svg width="10" height="10" viewBox="0 0 10 10"><path d="M3.5 1.5 7 5 3.5 8.5" stroke="#14146a" fill="none" stroke-width="1.3"/></svg></div>
  <div class="abs seal"></div>
</section>

<section>
  <div class="abs about-photo" role="img" aria-label="Refrigerated warehouse with orange racking and pallets of stacked produce boxes"></div>
  <p class="abs eyebrow">Welcome to</p>
  <h2 class="abs about-title">Harborline Provisions</h2>
  <p class="abs about-lead">Harborline Provisions works with food manufacturers, brand owners, distributors and wholesalers market their products.</p>
  <p class="abs about-sub">Retail, Food Service and Industrial ingredients.</p>
  <p class="abs about-body">Founded in 2008, Harborline Provisions started with the distribution of gluten free products understanding the need to provide access to unique flavors and products for the celiac consumers. From this, we expanded into deli, dairy, groceries, frozen and beverages.</p>
  <a class="abs btn btn-orange about-cta" href="#">About Us</a>
</section>

<section>
  <div class="abs services"></div>
  <h2 class="abs services-title">What We Do</h2>
  <article class="abs card" style="left:88px">
    <div class="card-img img-sales" role="img" aria-label="Shop staff smiling behind a bakery counter"></div>
    <div class="card-cover"></div>
    <h3 class="card-title">Sales &amp; Marketing</h3>
    <p class="card-text">We connect food buyers and sellers through a dedicated approach.</p>
    <a class="btn btn-white card-btn" href="#">More</a>
  </article>
  <article class="abs card" style="left:440px">
    <div class="card-img img-trade" role="img" aria-label="Container ship loading at a port with cranes"></div>
    <div class="card-cover"></div>
    <h3 class="card-title">Trading</h3>
    <p class="card-text">We purchase goods anywhere and ship them Nationwide and Export.</p>
    <a class="btn btn-orange card-btn" href="#">More</a>
  </article>
  <article class="abs card" style="left:792px">
    <div class="card-img img-shelf" role="img" aria-label="Supermarket aisle with fully stocked shelves"></div>
    <div class="card-cover"></div>
    <h3 class="card-title">Closeout/Excess Inventory</h3>
    <p class="card-text">we buy closeouts and excess inventory for prisons, outlet stores and discounters.</p>
    <a class="btn btn-white card-btn" href="#">More</a>
  </article>
</section>

<section>
  <h2 class="abs why-title">Why Choose Us</h2>
  <p class="abs why-text">We pride ourselves in working in an easy, personal and accessible environment making our customers and vendors comfortable with us. We look forward to connecting with you and evaluating how we can assist you reaching your sales objectives.</p>
  <div class="abs feature" style="left:243px">
    <div class="feature-icon"><svg width="30" height="30" viewBox="0 0 24 24" fill="none" stroke="#14146a" stroke-width="1.5"><path d="M3 14h18l-2 5H5z"/><path d="M6 14V9h12v5"/><path d="M9 9V6h6v3"/><path d="M12 3v3"/></svg></div>
    <p class="feature-label">Supply Security</p>
  </div>
  <div class="abs feature" style="left:500px">
    <div class="feature-icon"><svg width="30" height="30" viewBox="0 0 24 24" fill="none" stroke="#14146a" stroke-width="1.5"><path d="M12 2v20"/><path d="M17 6H9.5a3.5 3.5 0 0 0 0 7h5a3.5 3.5 0 0 1 0 7H6"/></svg></div>
    <p class="feature-label">Competitive Pricing</p>
  </div>
  <div class="abs feature" style="left:742px">
    <div class="feature-icon"><svg width="26" height="26" viewBox="0 0 24 24" fill="none" stroke="#14146a" stroke-width="1.7"><path d="M4 17v-5a8 8 0 0 1 16 0v5"/><rect x="3" y="14" width="4" height="6" rx="1"/><rect x="17" y="14" width="4" height="6" rx="1"/></svg></div>
    <p class="feature-label">Customer Focussed</p>
  </div>
</section>

<footer>
  <div class="abs footer"></div>
  <h4 class="abs f-head" style="left:89px">Harborline Provisions</h4>
  <h4 class="abs f-head" style="left:407px">Quick Links</h4>
  <h4 class="abs f-head" style="left:585px">Send Us Message</h4>
  <div class="abs f-call">Call Us:
    <svg width="19" height="19" viewBox="0 0 24 24" fill="none" stroke="#f9ab30" stroke-width="1.6"><path d="M22 16.9v3a2 2 0 0 1-2.2 2 19.8 19.8 0 0 1-8.6-3.1 19.5 19.5 0 0 1-6-6A19.8 19.8 0 0 1 2.1 4.2 2 2 0 0 1 4.1 2h3a2 2 0 0 1 2 1.7c.1.9.4 1.8.7 2.7a2 2 0 0 1-.5 2.1L8 9.8a16 16 0 0 0 6 6l1.3-1.3a2 2 0 0 1 2.1-.4c.9.3 1.8.6 2.7.7a2 2 0 0 1 1.7 2z"/></svg>
    <b>555-014-2291</b></div>
  <p class="abs f-mail">e. hello@harborlineprovisions.com</p>
  <p class="abs f-loc-label">Location:</p>
  <p class="abs f-loc">4410 Cedar Landing Rd Suite 12, Brookvale, NB 20418</p>
  <ul class="abs f-links"><li>Home</li><li>About Us</li><li>What We Do</li><li>Contact Us</li><li>Giving Back</li></ul>
  <div class="abs field f-name">Name</div>
  <div class="abs field f-phone">Phone</div>
  <div class="abs field f-email">Email</div>
  <div class="abs field f-msg">Message ...</div>
  <a class="abs btn btn-orange f-send" href="#">Send Message</a>
  <span class="abs social" style="left:89px"></span>
  <span class="abs social on" style="left:129px"></span>
  <span class="abs social" style="left:169px"></span>
  <span class="abs social" style="left:209px"></span>
  <p class="abs copy">© 2020 Harborline Provisions All Rights Reserved.</p>
  <svg class="abs to-top" width="30" height="36" viewBox="0 0 30 36" fill="none" stroke="#f9ab30" stroke-width="2.5"><path d="M15 3 27 33 15 25 3 33z"/></svg>
</footer>

</body>
</html>
```